Book Cover For Future Bestselling Entrepreneurship Book

The book is called:
Cart Levers: The Quick-Lane Method to Earn Side Income and Launch a Venture in Your Off Hours

Somewhere on the cover, I'd like to experiment with a call-out that says "Featuring 300+ Apps and Marketplaces".

Author: Dale Vantry

The theme of the book is how to add your own personal "Cart Levers" on pre-existing marketplaces to reach a wide audience of buyers quickly. As far as artwork, I was thinking of a prominent literal "buy button" on the cover:
http://imgvault.east2.cdn.plimrock-media.com/dailyharrow.com/content/assets/v3/editorial/a/b7/a9f3c2d1-48e6-11e1-bc55-002b5ddf7989/7e1923c4ab8f1.image.jpg

(doesn't have to be blue or look like that, could be an more "online" looking button.)

Take a look at some of the current bestselling business books:
https://www.quillmarto.com/Top-Sellers-Reader-Shelf-Business-Investing/tops/digital-text/267930422/ref=tp_bs_nav_rshelf_2_267715122#1

I like:
https://www.quillmarto.com/Week-Venture-Build-Before-Ready-ebook/dp/Q11PXGLC9T/ref=tp_bs_267930422_75
https://www.quillmarto.com/Craft-Calling-Tested-Finding-Made-ebook/dp/Q11RYTKD2V/ref=tp_bs_267930422_18

Main criteria is something, clean and professional that still looks good in thumbnail form. If the files are delivered in a format I can edit, that's a big bonus because I'll need to make a square version for the audiobook and front/spine/back-cover for the paperback.

Dimensions 3000x4800, 300dpi

Target Market(s)

Aspiring entrepreneurs, people who want to make or need to money outside of a traditional job.

Industry/Entity Type

Small Business

Font styles to use
Sans Serif

Requirements
Must have
• Prominent Cart Levers text and a large button graphic
Nice to have
• A callout that says "Featuring 300+ Apps and Marketplaces"

```html
<!DOCTYPE html>
<html lang="en">
<head>
<meta charset="utf-8">
<title>Cart Levers — Dale Vantry</title>
<link href="https://fonts.googleapis.com/css2?family=Bebas+Neue&family=PT+Sans+Narrow&display=swap" rel="stylesheet">
<style>
  :root {
    --band-dark: #17344a;
    --band-light: #2b6b8c;
    --title-deep: #6b0033;
    --title-bright: #9e0049;
    --navy: #13405f;
    --bg-top: #ffffff;
    --bg-bottom: #d6d6d6;
    --button-dark: #174a66;
    --button-light: #3f86a8;
    --white: #ffffff;
  }
  html, body {
    margin: 0;
    padding: 0;
    width: 750px;
    height: 1200px;
    overflow: hidden;
  }
  .cover {
    position: relative;
    width: 750px;
    height: 1200px;
    overflow: hidden;
    background: linear-gradient(to bottom, var(--bg-top) 0%, #f2f2f2 45%, var(--bg-bottom) 100%);
  }
  .callout-band {
    position: absolute;
    left: 0;
    top: 34px;
    width: 750px;
    height: 65px;
    background: linear-gradient(to right, var(--band-dark), var(--band-light));
    box-shadow: 0 3px 5px rgba(0,0,0,0.3);
    display: flex;
    align-items: center;
    justify-content: center;
  }
  .callout-text {
    font-family: "PT Sans Narrow", "Arial Narrow", sans-serif;
    font-size: 36px;
    color: var(--white);
    letter-spacing: 0.2px;
  }
  .title {
    margin: 0;
    font-weight: normal;
  }
  .title-line {
    position: absolute;
    left: 0;
    width: 750px;
    text-align: center;
    font-family: "Bebas Neue", "Oswald", sans-serif;
    line-height: 1;
    white-space: nowrap;
  }
  .title-main {
    top: 90px;
    font-size: 460px;
    color: var(--title-deep);
    transform: scaleX(0.8);
    transform-origin: center top;
  }
  .title-second {
    top: 461px;
    font-size: 188px;
    color: var(--title-bright);
  }
  .subtitle {
    position: absolute;
    left: 0;
    top: 640px;
    width: 750px;
    margin: 0;
    text-align: center;
    font-family: "PT Sans Narrow", "Arial Narrow", sans-serif;
    font-weight: normal;
    font-size: 32px;
    line-height: 40px;
    color: var(--navy);
  }
  .hero-button {
    position: absolute;
    left: 196px;
    top: 760px;
    width: 352px;
    height: 270px;
    border-radius: 22px;
    background: radial-gradient(ellipse at 45% 40%, var(--button-light), var(--button-dark) 75%);
    transform: rotate(-8deg);
  }
  .author {
    position: absolute;
    left: 0;
    top: 1078px;
    width: 750px;
    margin: 0;
    text-align: center;
    font-family: "Bebas Neue", "Oswald", sans-serif;
    font-weight: normal;
    font-size: 103px;
    line-height: 1;
    color: var(--navy);
  }
</style>
</head>
<body>
  <main class="cover">
    <div class="callout-band">
      <span class="callout-text">Featuring 300+ Apps and Marketplaces</span>
    </div>

    <h1 class="title">
      <span class="title-line title-main">CART</span>
      <span class="title-line title-second">LEVERS:</span>
    </h1>

    <h2 class="subtitle">The Quick-Lane Method to Earn Side Income<br>and Launch a Venture in Your Off Hours</h2>

    <div class="hero-button" role="img" aria-label="Glossy blue square push button labelled BUY, shown in perspective"></div>

    <p class="author">DALE VANTRY</p>
  </main>
</body>
</html>
```